Bright Path Therapies business cards and stationary

Need business cards and stationary designed to match previously made logo for for a new company based in Sydney NSW called 'Bright Path Therapies'.

We provide early intervention services and diagnostic assessment for children with disability and their families. I would like designs that are colourful and child friendly - possibly using feet/footprints/steps on a white background. The final design should communicate that we are family friendly, accepting and fun to work with.

Target Market(s)

Parents and Families
Teachers
Allied Health Professionals

Industry/Entity Type

Psychology

Contact Information for Business Card

Bright Path Therapies
www.brightpaththerapies.example
info@brightpaththerapies.example

Font styles to use
Sans Serif
Decorative
Script

Requirements
Must have
• Match the font and colour scheme of logo, along with footprint picture
Nice to have
• Clean and simple, while reflecting that I am working with families.
• Also- editable for when we make staff specific cards.

```html
<!DOCTYPE html>
<html lang="en">
<head>
<meta charset="utf-8">
<title>Bright Path Therapies – Business Card</title>
<link rel="stylesheet" href="https://fonts.googleapis.com/css2?family=Fira+Sans:wght@300;400&display=swap">
<style>
  :root {
    --white: #ffffff;
    --ink: #1a1a1a;
    --red: #ef4136;
    --red-soft: #f26a61;
    --green: #8dc63f;
    --teal: #2e9dab;
    --blue: #1177bb;
    --orange: #f7941d;
  }
  html, body {
    margin: 0;
    padding: 0;
    width: 1200px;
    height: 1200px;
    overflow: hidden;
    background: var(--white);
    font-family: "Fira Sans", sans-serif;
  }
  .canvas {
    position: relative;
    width: 1200px;
    height: 1200px;
  }
  .card {
    position: absolute;
    left: 80px;
    width: 1052px;
    border-radius: 80px;
    overflow: hidden;
    box-sizing: border-box;
  }
  /* Front */
  .card-front {
    top: 38px;
    height: 558px;
    background: var(--white);
    border: 1px solid var(--ink);
  }
  .brand {
    position: absolute;
    left: 92px;
    top: 160px;
    display: flex;
    align-items: center;
    gap: 40px;
  }
  .brand-dot {
    width: 190px;
    height: 190px;
    border-radius: 50%;
    background: var(--red);
    flex: none;
  }
  .brand-name {
    margin: 0;
    font-weight: 400;
    font-size: 66px;
    line-height: 1;
    color: var(--blue);
    letter-spacing: 1px;
  }
  .colour-bar {
    position: absolute;
    left: 0;
    right: 0;
    top: 460px;
    height: 34px;
    display: flex;
  }
  .colour-bar span { flex: 1; }
  .bar-green  { background: var(--green); }
  .bar-teal   { background: var(--teal); }
  .bar-blue   { background: var(--blue); }
  .bar-orange { background: var(--orange); }
  .bar-red    { background: var(--red); }

  /* Back */
  .card-back {
    top: 618px;
    height: 556px;
    background: var(--red);
  }
  .footprint-trail {
    position: absolute;
    left: 96px;
    top: 0;
    width: 240px;
    height: 100%;
    background: var(--red-soft);
  }
  .contact {
    position: absolute;
    right: 64px;
    top: 258px;
    text-align: right;
    color: var(--white);
  }
  .contact-name {
    margin: 0;
    font-weight: 400;
    font-size: 37px;
    line-height: 54px;
    letter-spacing: 0.3px;
  }
  .contact-line {
    margin: 0;
    font-weight: 300;
    font-size: 36px;
    line-height: 54px;
    letter-spacing: 0.5px;
  }
</style>
</head>
<body>
<main class="canvas">
  <section class="card card-front" aria-label="Business card front">
    <div class="brand">
      <div class="brand-dot"></div>
      <h1 class="brand-name">Bright Path Therapies</h1>
    </div>
    <div class="colour-bar">
      <span class="bar-green"></span>
      <span class="bar-teal"></span>
      <span class="bar-blue"></span>
      <span class="bar-orange"></span>
      <span class="bar-red"></span>
    </div>
  </section>

  <section class="card card-back" aria-label="Business card back">
    <div class="footprint-trail" role="img" aria-label="Trail of white child footprints walking up the card"></div>
    <div class="contact">
      <p class="contact-name">BRIGHT PATH THERAPIES</p>
      <p class="contact-line">info@brightpaththerapies.example</p>
      <p class="contact-line">www.brightpaththerapies.example</p>
    </div>
  </section>
</main>
</body>
</html>
```